Sales Prospecting Card

This project is for a two sided 8 1/2" x 5 1/2" heavy stock, gloss card to be used by sales people in the field. Attached is a sample from another company, our logo, AND the copy we want on our card. Simple graphics, high readability desired. No photography. Colors similar to our logo...see our website www.vorundex.com for more information on who we are and what we do.

Target Market(s)

sales people targeting telecommunications professionals

Industry/Entity Type

Telecommunications

Requirements
Should not have
• Don't use photography for graphics.

```html
<!DOCTYPE html>
<html lang="en">
<head>
<meta charset="utf-8">
<title>Vorundex – Selling CallHaven Prospecting Card</title>
<link href="https://fonts.googleapis.com/css2?family=Open+Sans:wght@400;600;700&display=swap" rel="stylesheet">
<style>
  :root {
    --brand-blue: #1552a8;
    --brand-blue-dark: #0f4190;
    --page-bg: #e9eaec;
    --card-top: #ffffff;
    --card-bottom: #e6e6e6;
    --panel-top: #e4e4e4;
    --panel-bottom: #cfcfcf;
    --ink: #2e2e2e;
    --ink-soft: #4a4a4a;
    --icon: #3a3a3a;
  }
  * { box-sizing: border-box; margin: 0; padding: 0; }
  html, body { width: 1200px; height: 1200px; overflow: hidden; }
  body {
    background: var(--page-bg);
    font-family: "Open Sans", Arial, sans-serif;
    color: var(--ink);
    position: relative;
  }
  .card {
    position: absolute;
    left: 170px;
    width: 860px;
    height: 556px;
    background: linear-gradient(180deg, var(--card-top), var(--card-bottom));
    box-shadow: 0 6px 18px rgba(0,0,0,.18);
    overflow: hidden;
  }
  .card--front { top: 30px; }
  .card--back { top: 614px; }

  .card__header {
    position: absolute; left: 0; top: 0; width: 100%; height: 58px;
    background: var(--brand-blue);
  }
  .card__title {
    position: absolute; right: 62px; top: 32px;
    color: #fff; font-size: 15px; font-weight: 600; letter-spacing: .2px;
  }
  .brand-tab {
    position: absolute; left: 116px; top: 0; width: 150px; height: 62px;
    background: #fff;
    display: flex; align-items: center; justify-content: center; gap: 8px;
  }
  .brand-tab__mark { width: 14px; height: 14px; background: var(--brand-blue); }
  .brand-tab__name { font-size: 20px; font-weight: 700; color: var(--brand-blue); }

  .questions { position: absolute; left: 40px; top: 86px; width: 340px; }
  .questions h2 { font-size: 15px; font-weight: 600; margin-bottom: 18px; }
  .questions ul { list-style: none; }
  .questions li {
    font-size: 10.6px; line-height: 12.6px; color: var(--ink-soft);
    padding-left: 12px; position: relative; margin-bottom: 5px;
  }
  .questions li::before {
    content: ""; position: absolute; left: 0; top: 4px;
    width: 5px; height: 5px; border-radius: 50%; background: var(--ink);
  }

  .panel {
    position: absolute;
    background: linear-gradient(180deg, var(--panel-top), var(--panel-bottom));
    padding: 8px 10px;
  }
  .panel h3 { font-size: 12.5px; font-weight: 600; margin-bottom: 5px; }
  .panel p, .panel li {
    font-size: 9.4px; line-height: 12.4px; color: var(--ink-soft); list-style: none;
  }
  .panel .icon { position: absolute; right: 18px; }
  .panel .icon svg { display: block; }

  .panel--about { left: 386px; top: 64px; width: 458px; height: 86px; }
  .panel--comms { left: 386px; top: 156px; width: 458px; height: 172px; }
  .panel--outages { left: 386px; top: 334px; width: 458px; height: 168px; }

  .front-band {
    position: absolute; left: 0; bottom: 0; width: 100%; height: 48px;
    background: var(--brand-blue);
    color: #fff; font-size: 10px; line-height: 14px; padding: 10px 16px;
  }

  .panel--challenges { left: 20px; top: 74px; width: 410px; height: 214px; }
  .panel--benefits { left: 436px; top: 74px; width: 404px; height: 214px; }
  .panel--costs { left: 20px; top: 294px; width: 410px; height: 206px; }
  .panel--opportunities { left: 436px; top: 294px; width: 404px; height: 206px; }
  .panel--challenges li { line-height: 18.6px; font-size: 10px; }
  .panel--benefits li { font-size: 10px; line-height: 14px; margin-bottom: 17px; margin-top: 2px; }
  .panel--costs li { font-size: 10px; line-height: 22.4px; }
  .panel--opportunities li { font-size: 10px; line-height: 19.4px; }
  .panel--back h3 { font-size: 13px; margin-bottom: 8px; }

  .back-footer {
    position: absolute; left: 0; bottom: 0; width: 100%; height: 50px;
    background: var(--brand-blue); color: #fff;
    display: flex; justify-content: space-between; align-items: center;
    padding: 0 44px 0 36px; font-size: 12.5px;
  }
</style>
</head>
<body>

<section class="card card--front">
  <div class="card__header"><span class="card__title">SELLING CallHaven</span></div>
  <div class="brand-tab"><span class="brand-tab__mark"></span><span class="brand-tab__name">Vorundex</span></div>

  <div class="questions">
    <h2>Key Questions To Ask The Prospect</h2>
    <ul>
      <li>How effective is your current backup plan at providing alternate forms of communication beyond voice?</li>
      <li>Does your current backup plan rely on the public infrastructure (secondary carrier, last mile connection, etc.)?</li>
      <li>What is the potential financial impact if your business lost telecommunications for several hours, days?</li>
      <li>Is your current backup plan always on or does it require activation by a third party?</li>
      <li>Is your current backup plan static? How difficult is it to make changes on-the-fly? How difficult is it to activate your backup communication plan?</li>
      <li>On a scale of 1 to 10, How beneficial would the ability to send incoming calls to any of the following? Cell, desk, Talkwell, alternate locations?</li>
      <li>Does your hospital comply with the Medicare / Medicaid requirements for backup communications?</li>
      <li>Given the current transition of 9-1-1 networks to Next Generation, can your telecommunications withstand the predicted increase</li>
    </ul>
  </div>

  <div class="panel panel--about">
    <h3>CallHaven</h3>
    <p>Backup an entire phone system with 24/7 OB and/or IB<br>solutions for any environment.<br>Cloud-based or connected to your PBX. Alternate path connectivity<br>with high quality, DOD grade Satellite and/or Internet.</p>
    <span class="icon" style="top:18px">
      <svg width="44" height="54" viewBox="0 0 44 54" fill="none" stroke="var(--icon)" stroke-width="3.4" stroke-linejoin="round"><path d="M4 8 Q22 2 40 8 V30 Q36 44 22 51 Q8 44 4 30 Z"/></svg>
    </span>
  </div>

  <div class="panel panel--comms">
    <h3>Effective Communication</h3>
    <ul>
      <li>Full suite of features to help achieve Continuity of Operations (COOP)</li>
      <li>- Real-time control</li>
      <li>- Auto-attendant/Integrated Voice Response (IVR)</li>
      <li>- Find me/Follow me</li>
      <li>- Voicemail/Fax recovery</li>
      <li>- Conference Bridge</li>
      <li>- Boomerang</li>
      <li>- Unlimited Directory</li>
      <li>- Uniform Call Distribution (UCD)</li>
      <li>- Pre-recorded hotlines</li>
      <li>- OCN/DID Functionality</li>
    </ul>
    <span class="icon" style="top:70px">
      <svg width="54" height="48" viewBox="0 0 54 48" fill="none" stroke="var(--icon)" stroke-width="3.2" stroke-linejoin="round"><path d="M22 4 C10 4 3 11 3 18 C3 23 6 27 10 29 L7 37 L17 31 C19 32 21 32 22 32 C34 32 41 25 41 18 C41 11 34 4 22 4 Z"/><path d="M44 16 C49 19 51 23 51 26 C51 30 49 33 45 35 L47 43 L39 38 C35 39 30 38 27 36"/></svg>
    </span>
  </div>

  <div class="panel panel--outages">
    <h3>Cover All Outages</h3>
    <ul>
      <li>Effective solutions combined with industry leading Best Practices.</li>
      <li>Works in any environment during major and minor outages.</li>
      <li>- Carrier Failure</li>
      <li>- Equipment Failure</li>
      <li>- Last mile</li>
      <li>- Natural Disaster</li>
      <li>- Power Failure</li>
      <li>- Evacuation</li>
    </ul>
    <span class="icon" style="top:56px">
      <svg width="62" height="62" viewBox="0 0 62 62" fill="none" stroke="var(--icon)" stroke-width="3.6"><circle cx="31" cy="31" r="27"/><path d="M22 22 H40 V32 Q40 40 31 40 Q22 40 22 32 Z" fill="var(--icon)"/><path d="M26 22 V14 M36 22 V14 M31 40 V48"/><path d="M12 12 L50 50" stroke="var(--panel-bottom)" stroke-width="7"/><path d="M12 12 L50 50"/></svg>
    </span>
  </div>

  <div class="front-band">
    Get calls to the people they were meant for with an easy to use, sophisticated solution that keeps organizations communicating effectively during disruptions large and small.<br>
    100% add-on solution to primary communications – replaces no existing equipment or service.
  </div>
</section>

<section class="card card--back">
  <div class="card__header"><span class="card__title">SELLING CallHaven</span></div>
  <div class="brand-tab"><span class="brand-tab__mark"></span><span class="brand-tab__name">Vorundex</span></div>

  <div class="panel panel--back panel--challenges">
    <h3>Common Voice Recovery Challenges.</h3>
    <ul>
      <li>Bad experience with handheld satellite phones.</li>
      <li>Backup carrier in place (still reliant on primary carrier and infrastructure).</li>
      <li>Budget is lean with little to no existing DR/Continuity products.</li>
      <li>Continuity/DR is viewed as nice, but not “must have”.</li>
      <li>Identifying/communicating with the right people.</li>
      <li>Concern over time consumption to implement.</li>
      <li>Concern about learning a new “system”.</li>
      <li>Worry about solutions with escalating charges if the system is used.</li>
      <li>Ease of use.</li>
    </ul>
  </div>

  <div class="panel panel--back panel--benefits">
    <h3>Key Benefits</h3>
    <ul>
      <li>Always on, always ready.</li>
      <li>Maintain a fluid presence with outside caller.</li>
      <li>Maintain critical employee communication.</li>
      <li>Real-time control</li>
      <li>Easy to implement and use.</li>
    </ul>
    <span class="icon" style="top:62px">
      <svg width="34" height="68" viewBox="0 0 34 68" fill="none" stroke="var(--icon)" stroke-width="3.4" stroke-linejoin="round"><circle cx="17" cy="15" r="12"/><path d="M13 27 V60 L17 65 L21 60 V54 L17 51 L21 47 L17 43 L21 39 V27"/></svg>
    </span>
  </div>

  <div class="panel panel--back panel--costs">
    <h3>Potential Cost Offsets</h3>
    <ul>
      <li>Elimination of redundant services:</li>
      <li>- Conference Bridge.</li>
      <li>- Secondary Carrier.</li>
      <li>- Outbound Notification.</li>
      <li>- 3<sup style="font-size:6px">rd</sup> party messaging service.</li>
      <li>- Analog backup phone conversion (satellite).</li>
      <li>- Reduce cost associated with other hardware redundancy.</li>
    </ul>
    <span class="icon" style="top:68px; right:26px">
      <svg width="36" height="58" viewBox="0 0 36 58" fill="none" stroke="var(--icon)" stroke-width="3.4" stroke-linecap="round"><path d="M18 2 V56"/><path d="M31 14 Q28 8 18 8 Q6 8 6 17 Q6 25 18 28 Q31 31 31 40 Q31 49 18 49 Q7 49 4 42"/></svg>
    </span>
  </div>

  <div class="panel panel--back panel--opportunities">
    <h3>Identifying Opportunities</h3>
    <ul>
      <li>- Organizations focused on Continuity of Operations (COOP)</li>
      <li>- Implementation of new voice technology (at cutover)</li>
      <li>- Recent disruption.</li>
      <li>- Technologically progressive.</li>
      <li>- Any industry where losing communications can mean lives or dollars lost.</li>
      <li>- Industries that have regulations or accreditation related to backup communications.</li>
    </ul>
  </div>

  <div class="back-footer">
    <span>www.vorundex.com</span>
    <span>© 2015 Vorundex, inc.</span>
  </div>
</section>

</body>
</html>
```